Client Fulfillment Flyer

This is a document used for internal purposes ie it is not distributed to clients. We would like it to have some colour, images etc. We are in the financial services industry, Ballarat, Victoria, Australia. www.tarrowfield.com.au and www.tarrowfieldagri.com.au

Target Market(s)

Internal training document

Industry/Entity Type

Finance And Accounting

Colors
3176b5

```html
<!DOCTYPE html>
<html lang="en">
<head>
<meta charset="utf-8">
<title>Tarrowfield &amp; Co – Team Roles</title>
<link href="https://fonts.googleapis.com/css2?family=Fira+Sans:wght@400;600;700&display=swap" rel="stylesheet">
<style>
  :root{
    --brand:#1f6fe0;
    --brand-dark:#1a5fc4;
    --ink:#4a5659;
    --label:#4c5558;
    --rule:#dfe3e4;
    --col-grey:#e6eaea;
    --col-cyan:#c9fbf5;
    --row-shade:#f4f5f5;
    --tick:#4cd64c;
  }
  *{box-sizing:border-box;margin:0;padding:0}
  html,body{width:939px;height:1200px;overflow:hidden;background:#fff}
  body{position:relative;font-family:"Fira Sans",Arial,sans-serif;color:var(--ink)}

  .masthead{position:absolute;left:77px;top:60px;width:793px;height:32px;display:flex;align-items:center}
  .brand-dot{width:32px;height:32px;border-radius:50%;background:var(--brand);flex:none}
  .brand-name{margin-left:7px;font-weight:700;font-size:19px;letter-spacing:.5px;color:var(--brand);white-space:nowrap}
  .masthead-rule{flex:1;height:1px;background:var(--rule);margin-left:14px}

  .intro{position:absolute;left:142px;top:150px;width:660px;font-size:14px;line-height:20px;letter-spacing:.2px;color:var(--ink)}

  .roles{position:absolute;left:142px;top:227px;width:657px}
  .grid{display:grid;grid-template-columns:293px 85px 85px 86px 84px;column-gap:6px}
  .head .role{height:52px;margin-bottom:3px;background:var(--brand);border-radius:6px 6px 0 0;color:#fff;
    font-weight:700;font-size:11px;letter-spacing:.9px;line-height:13.5px;display:flex;align-items:center;justify-content:center;text-align:center;
    box-shadow:0 2px 0 var(--brand-dark)}
  .head .blank{background:none}
  .row .task{padding-left:16px;font-size:11.5px;line-height:17.5px;color:var(--label);display:flex;align-items:center;letter-spacing:.2px}
  .row .c{display:flex;align-items:center;justify-content:center}
  .row .grey{background:var(--col-grey)}
  .row .cyan{background:var(--col-cyan)}
  .row.shade .task{background:var(--row-shade)}
  .row.shade .grey{background:#e2e6e6}
  .row.shade .cyan{background:#c6f4ef}
  .tick{width:19px;height:19px}

  .folio{position:absolute;left:77px;top:1125px;width:793px;height:1px;background:var(--rule)}
  .folio-num{position:absolute;left:451px;top:1105px;width:38px;height:38px;border-radius:50%;background:#fff;border:1px solid var(--rule);display:flex;align-items:center;justify-content:center}
  .folio-num span{width:32px;height:32px;border-radius:50%;background:var(--brand);color:#fff;font-size:17px;display:flex;align-items:center;justify-content:center}
</style>
</head>
<body>
<svg width="0" height="0" style="position:absolute">
  <defs>
    <symbol id="tick" viewBox="0 0 20 20">
      <circle cx="10" cy="10" r="10" fill="#4cd64c"/>
      <path d="M5.5 10.3l3 3 6-6.3" fill="none" stroke="#fff" stroke-width="2.2" stroke-linecap="round" stroke-linejoin="round"/>
    </symbol>
  </defs>
</svg>

<header class="masthead">
  <div class="brand-dot"></div>
  <div class="brand-name">TARROWFIELD &amp; CO</div>
  <div class="masthead-rule"></div>
</header>

<p class="intro">Below is a table of the many jobs and tasks we do on a daily basis and the team member role that is responsible for that task.</p>

<section class="roles">
  <div class="grid head">
    <div class="role blank"></div>
    <div class="role">CSM</div>
    <div class="role">Manila<br>Accountant</div>
    <div class="role">Accountant</div>
    <div class="role">Senior<br>Manager/<br>Partner</div>
  </div>

  <div class="grid row shade" style="height:35px"><div class="task">Contacting clients for missing information</div><div class="c grey"><svg class="tick"><use href="#tick"/></svg></div><div class="c cyan"></div><div class="c grey"></div><div class="c cyan"></div></div>
  <div class="grid row" style="height:28px"><div class="task">Changes to database / CRM</div><div class="c grey"><svg class="tick"><use href="#tick"/></svg></div><div class="c cyan"></div><div class="c grey"></div><div class="c cyan"></div></div>
  <div class="grid row shade" style="height:35px"><div class="task">Returning client records</div><div class="c grey"><svg class="tick"><use href="#tick"/></svg></div><div class="c cyan"></div><div class="c grey"></div><div class="c cyan"></div></div>
  <div class="grid row" style="height:29px"><div class="task">Preparing Balance Date Checklists</div><div class="c grey"><svg class="tick"><use href="#tick"/></svg></div><div class="c cyan"></div><div class="c grey"></div><div class="c cyan"></div></div>
  <div class="grid row shade" style="height:45px"><div class="task">Fee proposal draft preparation and send to client<br>once final</div><div class="c grey"><svg class="tick"><use href="#tick"/></svg></div><div class="c cyan"></div><div class="c grey"></div><div class="c cyan"></div></div>
  <div class="grid row" style="height:34px"><div class="task">Job set up</div><div class="c grey"><svg class="tick"><use href="#tick"/></svg></div><div class="c cyan"></div><div class="c grey"></div><div class="c cyan"></div></div>
  <div class="grid row shade" style="height:45px"><div class="task">Confirm fee proposal details, explain benefit to<br>client and value</div><div class="c grey"></div><div class="c cyan"></div><div class="c grey"><svg class="tick"><use href="#tick"/></svg></div><div class="c cyan"><svg class="tick"><use href="#tick"/></svg></div></div>
  <div class="grid row" style="height:37px"><div class="task">Setting Due Dates for all jobs in workflow program</div><div class="c grey"><svg class="tick"><use href="#tick"/></svg></div><div class="c cyan"></div><div class="c grey"></div><div class="c cyan"></div></div>
  <div class="grid row shade" style="height:45px"><div class="task">Collating information to send to banks, finance<br>co’s etc, and sending once confirmed.</div><div class="c grey"><svg class="tick"><use href="#tick"/></svg></div><div class="c cyan"></div><div class="c grey"></div><div class="c cyan"></div></div>
  <div class="grid row" style="height:50px"><div class="task">Setting and managing Start Dates and To-do Dates<br>in workflow program</div><div class="c grey"></div><div class="c cyan"></div><div class="c grey"><svg class="tick"><use href="#tick"/></svg></div><div class="c cyan"></div></div>
  <div class="grid row shade" style="height:45px"><div class="task">Manage workflow to meet client expectations and<br>team sales budget</div><div class="c grey"></div><div class="c cyan"></div><div class="c grey"><svg class="tick"><use href="#tick"/></svg></div><div class="c cyan"><svg class="tick"><use href="#tick"/></svg></div></div>
  <div class="grid row" style="height:55px"><div class="task">Communicate workflow concerns and bottlenecks<br>before they become an issue</div><div class="c grey"></div><div class="c cyan"></div><div class="c grey"><svg class="tick"><use href="#tick"/></svg></div><div class="c cyan"></div></div>
  <div class="grid row shade" style="height:35px"><div class="task">Dealing with ATO correspondence</div><div class="c grey"><svg class="tick"><use href="#tick"/></svg></div><div class="c cyan"></div><div class="c grey"></div><div class="c cyan"></div></div>
  <div class="grid row" style="height:38px"><div class="task">Contacting the ATO</div><div class="c grey"><svg class="tick"><use href="#tick"/></svg></div><div class="c cyan"></div><div class="c grey"></div><div class="c cyan"></div></div>
  <div class="grid row shade" style="height:45px"><div class="task">Advising clients of PAYG instalment amounts and<br>due dates</div><div class="c grey"><svg class="tick"><use href="#tick"/></svg></div><div class="c cyan"></div><div class="c grey"></div><div class="c cyan"></div></div>
  <div class="grid row" style="height:41px"><div class="task">Printing, binding financial statements, tax returns<br>and reports etc</div><div class="c grey"><svg class="tick"><use href="#tick"/></svg></div><div class="c cyan"></div><div class="c grey"></div><div class="c cyan"></div></div>
  <div class="grid row shade" style="height:34px"><div class="task">Advising clients of TFN, ABN, GST registrations etc</div><div class="c grey"><svg class="tick"><use href="#tick"/></svg></div><div class="c cyan"></div><div class="c grey"></div><div class="c cyan"></div></div>
  <div class="grid row" style="height:34px"><div class="task">Advising clients of tax assessment notices</div><div class="c grey"><svg class="tick"><use href="#tick"/></svg></div><div class="c cyan"></div><div class="c grey"></div><div class="c cyan"></div></div>
  <div class="grid row shade" style="height:35px"><div class="task">Invoicing and job completion</div><div class="c grey"><svg class="tick"><use href="#tick"/></svg></div><div class="c cyan"></div><div class="c grey"></div><div class="c cyan"></div></div>
</section>

<div class="folio"></div>
<div class="folio-num"><span>5</span></div>
</body>
</html>
```